Business Card Design - R.T. Custom Cabinets Ltd.

Design a business card, including a new logo for a new company in Vancouver, British Columbia, Canada.

The logo must be available as a separate file.

The card should include all company information including:
R.T. Custom Cabinets Ltd.
5826 Larkspur Avenue
Burnaby, B.C. V7K 2P9
Telehone: 604-555-0173
Fax: 604-555-0173
www.rtcustomcabinets.example

As well as individual contact information for employees:
Name
Position
Telephone
Email

The card must include a thoughtful message as well

Target Market(s)

Custom Cabinets

Industry/Entity Type

Business

Contact Information for Business Card

Important information on the front, thoughtful message on the back

Colors
fbed22
9bcb3c
0355a3
ec1f27

Requirements
Must have
• See project description
Nice to have
• images that showcase custom cabinets (european, modern and traditional) styles

```html
<!DOCTYPE html>
<html lang="en">
<head>
<meta charset="utf-8">
<title>R.T. Custom Cabinets Ltd. – Business Card</title>
<link href="https://fonts.googleapis.com/css2?family=Lato:wght@400;700;900&family=Roboto+Condensed:wght@700&display=swap" rel="stylesheet">
<style>
  :root{
    --blue:#0d56a6;
    --green:#9bcb3c;
    --ink:#3a3a3a;
    --paper:#ffffff;
    --backdrop:#ece9e4;
  }
  *{margin:0;padding:0;box-sizing:border-box}
  html,body{width:1200px;height:1000px;overflow:hidden}
  body{background:var(--backdrop);position:relative;font-family:'Lato',sans-serif}
  .card{position:absolute;width:526px;height:300px;overflow:hidden;box-shadow:0 4px 14px rgba(0,0,0,.18)}
  .card--front{left:152px;top:160px;background:var(--paper)}
  .card--back{left:496px;top:513px;background:var(--blue)}

  .brand{position:absolute;display:flex;align-items:center;gap:10px}
  .brand__mark{width:18px;height:18px;flex:none}
  .brand__name{font-family:'Roboto Condensed',sans-serif;font-weight:700;text-transform:uppercase;line-height:1.1}
  .card--front .brand{left:36px;top:128px;width:200px}
  .card--front .brand__mark{background:var(--green)}
  .card--front .brand__name{color:var(--blue);font-size:18px}

  .divider{position:absolute;left:245px;top:73px;width:1.5px;height:133px;background:#444}

  .person{position:absolute;left:278px;top:67px}
  .person__name{font-weight:900;font-size:21px;color:var(--blue);letter-spacing:.2px}
  .person__name span{color:var(--green)}
  .person__role{font-size:15px;color:var(--ink);margin-top:1px}
  .contacts{list-style:none;margin-top:13px}
  .contacts li{display:flex;align-items:center;gap:8px;font-size:13px;color:var(--ink);height:17px}
  .contacts svg{width:11px;height:11px;fill:var(--blue);flex:none}

  .band{position:absolute;inset:0;width:526px;height:300px}

  .card--back .brand{left:0;right:0;top:98px;justify-content:center}
  .card--back .brand__mark{width:26px;height:26px;background:var(--paper)}
  .card--back .brand__name{color:var(--paper);font-size:30px;max-width:240px}
  .address{position:absolute;left:0;right:0;top:256px;text-align:center;color:var(--paper);font-size:12px}
</style>
</head>
<body>

<section class="card card--front" aria-label="Business card front">
  <div class="brand">
    <span class="brand__mark"></span>
    <span class="brand__name">R.T. Custom Cabinets Ltd</span>
  </div>
  <div class="divider"></div>
  <div class="person">
    <h1 class="person__name">JOHN <span>DOE</span></h1>
    <p class="person__role">Manager</p>
    <ul class="contacts">
      <li><svg viewBox="0 0 12 12"><path d="M3 0h6v12H3z M4 1v9h4V1z"/></svg>01 - 234 - 5679</li>
      <li><svg viewBox="0 0 12 12"><path d="M2 0l3 2-1 2c1 2 2 3 4 4l2-1 2 3-2 2C5 11 1 7 0 2z"/></svg>01 - 234 - 5679</li>
      <li><svg viewBox="0 0 12 12"><path d="M3 0h6v3H3z M0 4h12v5H9v3H3V9H0z M4 8v3h4V8z"/></svg>01 - 234 - 5679</li>
      <li><svg viewBox="0 0 12 12"><path d="M6 0a6 6 0 1 0 0 12A6 6 0 0 0 6 0zm0 1.2c.8 0 1.6 1.8 1.7 4.1H4.3C4.4 3 5.2 1.2 6 1.2zM1.2 6.7h2.1c.1 1.3.3 2.5.8 3.3a4.8 4.8 0 0 1-2.9-3.3zm0-1.4A4.8 4.8 0 0 1 4.1 2c-.5.8-.7 2-.8 3.3zm3.1 1.4h3.4C7.6 9 6.8 10.8 6 10.8S4.4 9 4.3 6.7zm4.4 0h2.1A4.8 4.8 0 0 1 7.9 10c.5-.8.7-2 .8-3.3zm0-1.4c-.1-1.3-.3-2.5-.8-3.3a4.8 4.8 0 0 1 2.9 3.3z"/></svg>www.rtcustomcabinets.example</li>
      <li><svg viewBox="0 0 12 12"><path d="M0 2h12v1L6 7 0 3z M0 4.5l6 4 6-4V10H0z"/></svg>youremailaddresss@domain.com</li>
    </ul>
  </div>
  <svg class="band" viewBox="0 0 526 300" aria-hidden="true">
    <polygon points="0,278 332,278 325,300 0,300" fill="var(--green)"/>
    <polygon points="338,270 526,270 526,300 327,300" fill="var(--blue)"/>
  </svg>
</section>

<section class="card card--back" aria-label="Business card back">
  <div class="brand">
    <span class="brand__mark"></span>
    <span class="brand__name">R.T. Custom Cabinets Ltd.</span>
  </div>
  <p class="address">5826 Larkspur Avenue,Burnaby, B.C. V7K 2P9</p>
</section>

</body>
</html>
```